Brightmark Pixel Collective Website

I need my website redesigned to look very modern with the latest services. Check out my old website for information: www.brightmarkpixelcollective.com

You can use the same site menu links

It doesn't need to have the Recent News section

Please use the yellow, black and grey color scheme

Target Market(s)

25-50 years in range. Small Business Owners

Industry/Entity Type

Group

Requirements
Must have
• Logo and similar color scheme to current website
• Modern, Modern, Modern! I want a very fresh and modern look
Should not have
• Boring Look

```html
<!DOCTYPE html>
<html lang="en">
<head>
<meta charset="utf-8">
<title>Brightmark Pixel Collective</title>
<link href="https://fonts.googleapis.com/css2?family=Lato:wght@300;400;700;900&display=swap" rel="stylesheet">
<style>
:root{
  --yellow:#f5b400;
  --yellow-soft:#ffc928;
  --ink:#1c1c1c;
  --dark:#242424;
  --darker:#161616;
  --text:#555;
  --muted:#8a8a8a;
  --line:#dedede;
  --pale:#f1f1f1;
  --white:#fff;
}
*{box-sizing:border-box;margin:0;padding:0}
html,body{width:1200px;height:4431px;overflow:hidden}
body{font-family:"Lato",Arial,sans-serif;color:var(--text);background:var(--white);position:relative}
section,header,footer{position:absolute;left:0;width:1200px}
.section-title{font-weight:300;font-size:40px;color:var(--ink);text-align:center}
.section-sub{font-size:13px;line-height:20px;color:var(--muted);text-align:center;margin:16px auto 0;width:560px}
.btn{display:inline-block;border:1px solid var(--yellow);color:var(--yellow);font-size:12px;letter-spacing:1px;text-transform:uppercase;padding:9px 22px}
.placeholder{display:block}

/* header + hero */
.hero{top:0;height:548px;background:linear-gradient(160deg,#6d6f72,#3b3d40 45%,#8d8f92);}
.hero-shade{position:absolute;inset:0;background:rgba(0,0,0,.35)}
.site-header{top:0;height:118px;background:rgba(20,20,20,.78);z-index:2}
.brand{position:absolute;left:60px;top:14px;width:170px;text-align:center}
.brand-mark{width:34px;height:34px;margin:0 auto 8px;background:var(--yellow)}
.brand-name{font-size:11px;font-weight:700;letter-spacing:1.5px;color:var(--yellow);text-transform:uppercase;line-height:14px}
.contact-strip{position:absolute;left:240px;top:12px;font-size:12px;color:#ddd;display:flex;gap:26px}
.contact-strip b{color:var(--yellow);font-weight:700}
.main-nav{position:absolute;right:90px;top:56px;display:flex;gap:6px}
.main-nav a{color:#eee;font-size:14px;padding:12px 18px;text-decoration:none}
.main-nav a.active{background:var(--yellow);color:var(--ink)}
.hero-copy{position:absolute;top:185px;width:100%;text-align:center;color:var(--white);z-index:1}
.hero-copy h1{font-weight:300;font-size:50px;line-height:56px}
.hero-copy h1 span{color:var(--yellow-soft)}
.hero-copy .btn{margin-top:50px;padding:12px 30px;font-size:15px;text-transform:none;letter-spacing:0}

/* welcome */
.welcome{top:548px;height:507px;background:var(--pale);padding-top:44px}
.intro-cards{display:flex;justify-content:center;gap:24px;margin-top:52px}
.intro-card{width:277px}
.intro-card .placeholder{height:160px;border:3px solid transparent}
.intro-card.featured .placeholder{border-color:var(--yellow)}
.intro-card h3{font-size:15px;color:var(--ink);margin:16px 0 8px;font-weight:700}
.intro-card.featured h3{color:var(--yellow)}
.intro-card p{font-size:12px;line-height:18px;color:var(--muted)}

/* services */
.expertise{top:1055px;height:535px;background:var(--white);padding-top:78px}
.service-grid{display:flex;justify-content:center;gap:30px;margin-top:56px}
.service{width:200px;text-align:center}
.service-icon{width:80px;height:80px;border-radius:50%;background:var(--ink);margin:0 auto;display:flex;align-items:center;justify-content:center}
.service.highlight .service-icon{background:var(--yellow)}
.service h3{font-size:19px;font-weight:400;color:var(--ink);margin:26px 0 12px}
.service.highlight h3{color:var(--yellow)}
.service p{font-size:12px;line-height:18px;color:var(--muted);height:90px}
.service .btn{font-size:10px;padding:6px 14px;margin-top:20px}
.service.highlight .btn{border-color:var(--ink);color:var(--ink)}

/* portfolio */
.portfolio{top:1590px;height:834px;background:var(--pale);padding-top:56px}
.portfolio-grid{position:absolute;top:175px;left:0;width:1200px;display:grid;grid-template-columns:repeat(5,240px);grid-auto-rows:205px}
.tile{position:relative}
.tile-feature{background:rgba(245,180,0,.9);display:flex;flex-direction:column;align-items:center;justify-content:center;color:var(--white);font-size:16px}
.tile-feature .plus{width:56px;height:56px;border:2px solid var(--white);border-radius:50%;margin-bottom:14px;display:flex;align-items:center;justify-content:center;font-size:34px;font-weight:300}

/* clients */
.clients{top:2424px;height:426px;background:var(--white);padding-top:32px}
.client-row{display:flex;justify-content:center;align-items:center;gap:44px;margin-top:44px}
.client{font-size:16px;font-weight:700;color:#333;letter-spacing:1px;text-transform:uppercase}
.client.boxed{background:#8c8c8c;color:var(--white);font-size:12px;padding:12px 18px;text-transform:lowercase}
.testimonial{width:910px;margin:40px auto 0;border:1px solid var(--line);padding:24px 30px;display:flex;gap:24px;box-shadow:0 2px 6px rgba(0,0,0,.06)}
.avatar{width:70px;height:70px;border-radius:50%;background:#c9c9c9;flex:none}
.testimonial p{font-size:12px;line-height:19px;color:var(--muted)}
.testimonial .byline{margin-top:10px;font-size:12px;color:var(--ink)}
.stars{color:var(--yellow);letter-spacing:2px;margin-right:6px}

/* news */
.news{top:2850px;height:720px;background:var(--pale);padding-top:32px}
.news-grid{width:920px;margin:58px auto 0;display:grid;grid-template-columns:repeat(3,1fr);row-gap:56px;column-gap:30px}
.news-item{display:flex;gap:16px}
.news-thumb{width:110px;height:120px;position:relative;flex:none;background:linear-gradient(#d5d0c4,#8c8676)}
.news-date{position:absolute;left:0;top:0;width:42px;background:var(--yellow);color:var(--white);text-align:center;font-size:15px;font-weight:700;line-height:18px;padding:4px 0}
.news-date small{display:block;font-size:9px;font-weight:400}
.news-item h4{font-size:14px;color:var(--ink);line-height:18px;margin-bottom:8px}
.news-item p{font-size:11px;line-height:16px;color:var(--muted)}
.news .center{text-align:center;margin-top:64px}

/* tweets */
.tweets{top:3570px;height:463px;background:linear-gradient(#6d6f72,#4a4c4f);text-align:center;color:var(--white)}
.tweets .bird{width:84px;height:84px;border-radius:50%;background:var(--yellow);margin:90px auto 18px}
.tweets h2{font-weight:300;font-size:28px}
.tweets p{font-size:14px;line-height:24px;width:760px;margin:18px auto 0;color:#e6e6e6}
.tweets p a{color:var(--yellow-soft);text-decoration:none}
.tweets .btn{margin-top:26px;font-size:11px}
.dots{margin-top:26px;display:flex;gap:8px;justify-content:center}
.dots i{width:9px;height:9px;border-radius:50%;background:#ccc}
.dots i.on{background:var(--yellow)}

/* help */
.help-bar{top:4033px;height:74px;background:var(--darker);color:var(--white);display:flex;align-items:center;justify-content:space-between;padding:0 160px}
.help-bar .ask{font-size:16px}
.help-bar .ask b{font-weight:700;margin-right:6px}
.help-bar .phone{font-size:30px;font-weight:700;display:flex;align-items:center;gap:12px}

/* footer */
.site-footer{top:4107px;height:278px;background:var(--dark);padding:44px 160px 0;display:flex;gap:46px;color:#bbb}
.footer-col h5{color:var(--white);font-size:14px;margin-bottom:14px}
.footer-col ul{list-style:none}
.footer-col li{font-size:12px;line-height:21px}
.footer-col li::before{content:"• ";color:var(--yellow)}
.footer-col li.current{color:var(--yellow)}
.newsletter p{font-size:12px;line-height:17px;width:220px}
.signup{display:flex;margin-top:12px}
.signup span{width:160px;height:30px;background:var(--white);font-size:11px;color:#999;padding:8px}
.signup b{background:var(--yellow);color:var(--ink);font-size:11px;padding:8px 14px}
.social{display:flex;gap:8px;margin-top:8px}
.social i{width:26px;height:26px;border-radius:50%;background:#555}
.bottom-bar{top:4385px;height:46px;background:var(--darker);color:#888;font-size:12px;display:flex;align-items:center;justify-content:space-between;padding:0 160px}
.bottom-bar nav{display:flex;gap:14px}
</style>
</head>
<body>

<section class="hero" role="img" aria-label="Photo of a team working at computers in a bright office">
  <div class="hero-shade"></div>
  <div class="hero-copy">
    <h1>We Provide<br><span>Website Design and Development</span><br><span>for Growth of Your Business</span></h1>
    <a class="btn">Learn More</a>
  </div>
</section>

<header class="site-header">
  <div class="brand">
    <div class="brand-mark"></div>
    <div class="brand-name">Brightmark Pixel<br>Collective</div>
  </div>
  <div class="contact-strip">
    <span>support@brightmarkpixelcollective.com</span>
    <span><b>TOLL FREE</b> 1 800 555 0142</span>
    <span><b>Local</b> 612 555 0188</span>
  </div>
  <nav class="main-nav">
    <a class="active">Home</a><a>Services ▾</a><a>Portfolio ▾</a><a>About Us ▾</a><a>Blog</a><a>Contact</a>
  </nav>
</header>

<section class="welcome">
  <h2 class="section-title">Welcome to Brightmark Pixel Collective</h2>
  <p class="section-sub">We build bright, modern websites for small businesses that want to stand out. Design, code and growth under one roof.</p>
  <div class="intro-cards">
    <article class="intro-card">
      <div class="placeholder" role="img" aria-label="Photo of colleagues meeting at a desk" style="background:linear-gradient(#dfe6ee,#9fb0c2)"></div>
      <h3>Our Mission</h3>
      <p>We help small business owners grow online with clear, fast and modern sites that turn visitors into loyal customers.</p>
    </article>
    <article class="intro-card featured">
      <div class="placeholder" role="img" aria-label="Photo of a team reviewing work together" style="background:linear-gradient(#e9e2d6,#b69f80)"></div>
      <h3>Our Vision</h3>
      <p>To be the trusted web partner for every growing business, pairing fresh design with tools that simply work every day.</p>
    </article>
    <article class="intro-card">
      <div class="placeholder" role="img" aria-label="Illustration of a cloud on a blue background" style="background:linear-gradient(#cfe4f6,#4f8fc8)"></div>
      <h3>Our Solution</h3>
      <p>Strategy, design, development and marketing handled by one small team, so your project stays simple from start to finish.</p>
    </article>
  </div>
</section>

<section class="expertise">
  <h2 class="section-title">We're experts in</h2>
  <div class="service-grid">
    <article class="service">
      <div class="service-icon"><svg width="38" height="38" viewBox="0 0 38 38" fill="none" stroke="#f5b400" stroke-width="3"><circle cx="19" cy="19" r="7"/><path d="M19 3v6M19 29v6M3 19h6M29 19h6M8 8l4 4M26 26l4 4M8 30l4-4M26 12l4-4"/></svg></div>
      <h3>Web Development</h3>
      <p>Custom sites built on clean code that load quickly, rank well and grow with your business over time.</p>
      <a class="btn">Learn more</a>
    </article>
    <article class="service">
      <div class="service-icon"><svg width="38" height="38" viewBox="0 0 38 38" fill="none" stroke="#f5b400" stroke-width="3"><path d="M6 13h26l-3 19H9z"/><path d="M13 13a6 6 0 0 1 12 0"/></svg></div>
      <h3>Amazing Online Stores</h3>
      <p>Stores that make buying easy, with simple checkout, stock tools and secure payments built right in.</p>
      <a class="btn">Learn more</a>
    </article>
    <article class="service highlight">
      <div class="service-icon"><svg width="38" height="38" viewBox="0 0 38 38" fill="#1c1c1c"><path d="M5 7h28v18H16l-7 7v-7H5z"/></svg></div>
      <h3>Social Media</h3>
      <p>Campaigns and content plans that grow your audience and keep customers talking about your brand.</p>
      <a class="btn">Learn more</a>
    </article>
    <article class="service">
      <div class="service-icon"><svg width="38" height="38" viewBox="0 0 38 38" fill="none" stroke="#f5b400" stroke-width="3"><rect x="5" y="5" width="28" height="28"/><path d="M12 27v-6M19 27V13M26 27v-10"/></svg></div>
      <h3>Online Marketing</h3>
      <p>Search, email and paid ads managed with care, so every budget brings real and measurable results.</p>
      <a class="btn">Learn more</a>
    </article>
  </div>
</section>

<section class="portfolio">
  <h2 class="section-title">Our Portfolio</h2>
  <p class="section-sub">A selection of recent sites, stores and apps we designed and built for clients across many fields.</p>
  <div class="portfolio-grid">
    <div class="tile" role="img" aria-label="Website project screenshot in dark blue" style="background:#1f3550"></div>
    <div class="tile" role="img" aria-label="Fashion store website screenshot" style="background:#3a3a3a"></div>
    <div class="tile" role="img" aria-label="Sports apparel campaign screenshot" style="background:#15171c"></div>
    <div class="tile" role="img" aria-label="App icon with a star on red" style="background:#a8322a"></div>
    <div class="tile" role="img" aria-label="Dark product site screenshot" style="background:#2b2b2b"></div>
    <div class="tile" role="img" aria-label="Mobile app shown on a phone" style="background:#23323f"></div>
    <div class="tile" role="img" aria-label="Gold product showcase page" style="background:#8b6a1f"></div>
    <div class="tile" role="img" aria-label="Colourful web page on a laptop" style="background:#5a4a6a"></div>
    <div class="tile" role="img" aria-label="Group portrait on a website banner" style="background:#8c7b6b"></div>
    <div class="tile" role="img" aria-label="Phone on a wooden desk" style="background:#4b3b2c"></div>
    <div class="tile" role="img" aria-label="Landing page with gold tones" style="background:#a07a2a"></div>
    <div class="tile tile-feature"><div class="plus">+</div>Media Design</div>
    <div class="tile" role="img" aria-label="Tablet interface design" style="background:#2d4a5c"></div>
    <div class="tile" role="img" aria-label="Product on a light background" style="background:#b7b2a8"></div>
    <div class="tile" role="img" aria-label="Hand holding a smartphone" style="background:#5e6a78"></div>
  </div>
</section>

<section class="clients">
  <h2 class="section-title">Some of Our Clients</h2>
  <p class="section-sub">Brands large and small trust us with their websites, stores and online marketing every day.</p>
  <div class="client-row">
    <span class="client boxed">zolvik</span>
    <span class="client">Brisolet</span>
    <span class="client">Kestrava Bank</span>
    <span class="client">Marrowind Group</span>
    <span class="client">Tolvenhaus</span>
    <span class="client">Quendrix</span>
  </div>
  <div class="testimonial">
    <div class="avatar" role="img" aria-label="Client portrait"></div>
    <div>
      <p>Working with this team was easy from day one. They listened, shared clear ideas and delivered a fresh site on time. Our online orders doubled within three months and our customers keep telling us how simple the new store is to use. We could not be happier.</p>
      <div class="byline"><span class="stars">★★★★★</span><b>Mara Ellison</b>, October 26, 2019</div>
    </div>
  </div>
</section>

<section class="news">
  <h2 class="section-title">Breaking News</h2>
  <p class="section-sub">Fresh updates from our studio, new launches and tips for growing your business online.</p>
  <div class="news-grid">
    <article class="news-item"><div class="news-thumb" role="img" aria-label="City skyline photo"><div class="news-date">16<small>JAN</small></div></div><div><h4>New site launch for a local bakery</h4><p>Fresh look, simple menu and online orders for a busy neighbourhood shop.</p></div></article>
    <article class="news-item"><div class="news-thumb" role="img" aria-label="City skyline photo"><div class="news-date">18<small>JAN</small></div></div><div><h4>Five tips for faster pages</h4><p>Small changes that help your site load quickly on every phone.</p></div></article>
    <article class="news-item"><div class="news-thumb" role="img" aria-label="City skyline photo"><div class="news-date">21<small>JAN</small></div></div><div><h4>Why mobile comes first</h4><p>Most visitors arrive on phones, so we design for them from the start.</p></div></article>
    <article class="news-item"><div class="news-thumb" role="img" aria-label="City skyline photo"><div class="news-date">24<small>JAN</small></div></div><div><h4>Our team is growing again</h4><p>Two new designers join us to help more small businesses shine.</p></div></article>
    <article class="news-item"><div class="news-thumb" role="img" aria-label="City skyline photo"><div class="news-date">27<small>JAN</small></div></div><div><h4>Email that people open</h4><p>Subject lines, timing and layouts that lift results for shops.</p></div></article>
    <article class="news-item"><div class="news-thumb" role="img" aria-label="City skyline photo"><div class="news-date">30<small>JAN</small></div></div><div><h4>A fresh look for our blog</h4><p>New guides, case studies and ideas posted every single week.</p></div></article>
  </div>
  <div class="center"><a class="btn">More news</a></div>
</section>

<section class="tweets" role="img" aria-label="Faded photo of a city skyline">
  <div class="bird"></div>
  <h2>New Tweets</h2>
  <p><a>brightmark.link/x7k2</a> Our new guide to simple online stores is live. Learn how to set up products, payments and shipping in one afternoon and start selling this week. <a>#smallbiz</a> <a>#webdesign</a></p>
  <a class="btn">Follow us</a>
  <div class="dots"><i class="on"></i><i></i><i></i><i></i></div>
</section>

<section class="help-bar">
  <div class="ask"><b>Need Help?</b> Call Us, Monday to Friday, 10 AM to 6PM</div>
  <div class="phone"><svg width="28" height="28" viewBox="0 0 24 24" fill="#fff"><path d="M6.6 10.8a15 15 0 0 0 6.6 6.6l2.2-2.2c.3-.3.7-.4 1-.2 1.1.4 2.3.6 3.6.6.6 0 1 .4 1 1V20c0 .6-.4 1-1 1A17 17 0 0 1 3 4c0-.6.4-1 1-1h3.5c.6 0 1 .4 1 1 0 1.3.2 2.5.6 3.6.1.3 0 .7-.2 1z"/></svg>01.23.45.67.89</div>
</section>

<footer class="site-footer">
  <div class="footer-col"><h5>Services</h5><ul><li>Online Stores</li><li>Social Media</li><li>Online Marketing</li><li class="current">Digital Strategy</li><li>Responsive Mobile Designs</li><li>Hosting &amp; Domain Registration</li></ul></div>
  <div class="footer-col"><h5>Online Marketing</h5><ul><li>Email Marketing</li><li>Search Engine Optimization</li><li>Paid Search Management</li></ul><h5 style="margin-top:14px">Web Development</h5><ul><li>Web Design</li><li>Content Management Systems</li><li>Web Application Development</li></ul></div>
  <div class="footer-col"><h5>About Us</h5><ul><li>Our Team</li><li>Careers</li><li>Affiliate</li><li>News</li><li>Blog</li><li>Testimonials</li></ul></div>
  <div class="footer-col newsletter"><h5>Newsletter Signup</h5><p>Sign up for our news to get tips and offers sent to you.</p><div class="signup"><span>email address</span><b>SUBMIT</b></div><h5 style="margin-top:22px">Stay Connected</h5><div class="social"><i></i><i></i><i></i><i></i><i></i></div></div>
</footer>

<section class="bottom-bar">
  <span>Copyright © 2019</span>
  <nav><span>Home</span><span>Services</span><span>Portfolio</span><span>About Us</span><span>Blog</span><span>Contact</span></nav>
</section>

</body>
</html>
```